Book Cover for self help book describing how to become the author of your life

I need a good resolution front cover for a book that is published through Brindlewick in Print and ebook format. I can design the spine and back cover myself so just need the front angle.
The book is titled "Chart New Mornings" and it's about writing your own story for how you want to live your life. The image I had in my mind was a pen writing out the title on the front in a script-like font, like actual handwriting.
I've included a very basic mock-up that I've done myself just to give the general idea. The cover requires three pieces of writing.
Title: Chart New Mornings
Subtitle: Step Into a Brighter Season
Author: Martin Olsfield
Female 35-55

```html
<!DOCTYPE html>
<html lang="en">
<head>
<meta charset="utf-8">
<title>Chart New Mornings — Martin Olsfield</title>
<link rel="stylesheet" href="https://fonts.googleapis.com/css2?family=Great+Vibes&display=swap">
<style>
  :root {
    --ink: #1c2a86;
    --parchment-edge: #d9b56e;
    --parchment-dark: #c99a4e;
    --paper-light: #f6e8c4;
    --paper-mid: #eed9a6;
    --paper-deep: #e2c68a;
    --photo-light: #f1d2c2;
    --photo-shade: #d8ab95;
  }
  html, body {
    margin: 0;
    padding: 0;
    overflow: hidden;
  }
  .cover {
    position: relative;
    width: 800px;
    height: 1200px;
    overflow: hidden;
    background: radial-gradient(ellipse at 50% 40%, var(--parchment-edge) 0%, var(--parchment-dark) 100%);
    font-family: "Great Vibes", cursive;
    color: var(--ink);
    word-spacing: 0.22em;
  }
  .cover__sheet {
    position: absolute;
    left: 10px;
    top: -40px;
    width: 770px;
    height: 1300px;
    transform: rotate(-2.5deg);
    transform-origin: 50% 50%;
    background: radial-gradient(ellipse at 50% 45%, var(--paper-light) 0%, var(--paper-mid) 75%, var(--paper-deep) 100%);
    box-shadow: 0 0 18px rgba(120, 80, 20, 0.35);
  }
  .cover__title {
    position: absolute;
    left: 0;
    top: 40px;
    width: 800px;
    margin: 0;
    text-align: center;
    font-weight: 400;
    line-height: 1;
  }
  .cover__title-top {
    display: block;
    font-size: 128px;
  }
  .cover__title-main {
    display: block;
    font-size: 172px;
    margin-top: 10px;
  }
  .cover__subtitle {
    position: absolute;
    left: 120px;
    top: 560px;
    width: 560px;
    margin: 0;
    text-align: center;
    font-size: 70px;
    line-height: 1.3;
    font-weight: 400;
  }
  .cover__author {
    position: absolute;
    left: 100px;
    top: 915px;
    width: 620px;
    margin: 0;
    text-align: center;
    font-size: 74px;
    font-weight: 400;
  }
  .cover__photo {
    position: absolute;
    left: 625px;
    top: 670px;
    width: 175px;
    height: 440px;
    background: linear-gradient(160deg, var(--photo-light) 0%, var(--photo-shade) 100%);
    opacity: 0.85;
  }
</style>
</head>
<body>
  <main class="cover">
    <div class="cover__sheet"></div>

    <h1 class="cover__title">
      <span class="cover__title-top">Chart New</span>
      <span class="cover__title-main">Mornings</span>
    </h1>

    <p class="cover__subtitle">Step Into a Brighter Season</p>

    <p class="cover__author">Martin Olsfield</p>

    <div class="cover__photo" role="img" aria-label="Photograph of a hand holding a pen, writing the subtitle"></div>
  </main>
</body>
</html>
```